Granite Ridge Holdings

I have a real estate investment business.

** I need editable vector files of the final design.

Industry/Entity Type

Real Estate

Contact Information for Business Card

I would like the card to be clear and direct with the company name and contact info. I would prefer not to have a design that is too busy (i.e., with excessive detail) in the business card.

Font styles to use
Sans Serif

Requirements
Must have
• My card must have the following information listed below:
• Company name: Grainite Ridge Holdings LLC
• My name: Daniel Vorsley
• Phone number: (555) 218-9067
• Email address: dtvorsley@mailbox-example.net
• Keywords: “Real Estate Investments”
Nice to have
• I would like to have a design that resembles the characteristics/uses of obsidian stone which resembles something related to strength and resilience. Perhaps something with sharp, sleek color transitions as well.

```html
<!DOCTYPE html>
<html lang="en">
<head>
<meta charset="utf-8">
<title>Granite Ridge Holdings – Business Card</title>
<link rel="stylesheet" href="https://fonts.googleapis.com/css2?family=Montserrat:wght@400;600;700&display=swap">
<style>
  :root {
    --ink: #000000;
    --paper: #ffffff;
    --glacier: #41b0cf;
    --backdrop: #ffffff;
  }
  * { margin: 0; padding: 0; box-sizing: border-box; }
  html, body {
    width: 1200px; height: 1200px; overflow: hidden;
    background: var(--backdrop);
    font-family: "Montserrat", sans-serif;
  }
  .sheet { position: relative; width: 1200px; height: 1200px; }
  .card {
    position: absolute; width: 686px; height: 381px; overflow: hidden;
  }
  .card svg.card-shapes { position: absolute; inset: 0; width: 100%; height: 100%; display: block; }
  .card--front { left: 278px; top: 153px; background: var(--paper); }
  .card--back { left: 272px; top: 626px; background: var(--ink); }

  .holder-name {
    position: absolute; left: 50px; top: 126px;
    font-weight: 700; font-size: 42px; color: var(--ink); letter-spacing: 0.5px;
    white-space: nowrap;
  }
  .contact-list { position: absolute; left: 54px; top: 229px; list-style: none; }
  .contact-item {
    display: flex; align-items: center; gap: 14px; height: 42px;
    font-size: 20px; color: var(--ink); white-space: nowrap;
  }
  .contact-icon { width: 26px; height: 26px; flex: none; }

  .wordmark {
    position: absolute; text-align: center; color: var(--glacier);
    font-weight: 600; white-space: nowrap; line-height: 1.1;
  }
  .wordmark__primary { display: block; letter-spacing: 1px; }
  .wordmark__secondary { display: block; letter-spacing: 1px; }
  .wordmark--front { left: 482px; top: 104px; width: 200px; }
  .wordmark--front .wordmark__primary { font-size: 20px; }
  .wordmark--front .wordmark__secondary { font-size: 11px; margin-top: 3px; }
  .wordmark--back { left: 0; width: 686px; top: 196px; }
  .wordmark--back .wordmark__primary { font-size: 38px; }
  .wordmark--back .wordmark__secondary { font-size: 16px; margin-top: 6px; }

  .tagline {
    position: absolute; left: 0; width: 686px; top: 348px; text-align: center;
    font-size: 19px; color: var(--glacier); font-weight: 400; letter-spacing: 0.3px;
  }
</style>
</head>
<body>
<main class="sheet">

  <section class="card card--front" aria-label="Business card front">
    <svg class="card-shapes" viewBox="0 0 858 477" preserveAspectRatio="none" aria-hidden="true">
      <polygon fill="var(--ink)" points="471,0 858,0 858,477 515,477 643,267"/>
      <polygon fill="var(--paper)" points="662,282 675,292 778,477 550,477"/>
      <polygon fill="var(--glacier)" points="643,267 662,282 550,477 515,477"/>
      <polygon fill="var(--ink)" points="668,300 678,314 578,477 558,477"/>
      <polygon fill="var(--glacier)" points="683,364 761,477 613,477"/>
    </svg>

    <div class="wordmark wordmark--front">
      <span class="wordmark__primary">GRAINITE RIDGE</span>
      <span class="wordmark__secondary">HOLDINGS LLC</span>
    </div>

    <h1 class="holder-name">Daniel Vorsley</h1>

    <ul class="contact-list">
      <li class="contact-item">
        <svg class="contact-icon" viewBox="0 0 26 26" aria-hidden="true">
          <circle cx="13" cy="13" r="13" fill="var(--ink)"/>
          <rect x="6.5" y="8.5" width="13" height="9" rx="1.5" fill="var(--paper)"/>
          <polyline points="7,9.5 13,14 19,9.5" fill="none" stroke="var(--ink)" stroke-width="1.5"/>
        </svg>
        <span>dtvorsley@mailbox-example.net</span>
      </li>
      <li class="contact-item">
        <svg class="contact-icon" viewBox="0 0 26 26" aria-hidden="true">
          <circle cx="13" cy="13" r="13" fill="var(--ink)"/>
          <path d="M9 7.5 L11.2 7 L12.2 10.2 L10.6 11.4 C11.3 13 12.6 14.4 14.4 15.3 L15.6 13.8 L18.8 14.9 L18.4 17.2 C17.8 18.4 16.3 18.9 14.8 18.4 C11.4 17.2 8.6 14.4 7.5 11 C7 9.6 7.6 8.1 9 7.5 Z" fill="var(--paper)"/>
        </svg>
        <span>(555) 218-9067</span>
      </li>
    </ul>
  </section>

  <section class="card card--back" aria-label="Business card back">
    <svg class="card-shapes" viewBox="0 0 858 477" preserveAspectRatio="none" aria-hidden="true">
      <polygon fill="var(--paper)" points="0,288 165,477 120,477 0,323"/>
      <polygon fill="var(--paper)" points="858,288 693,477 738,477 858,323"/>
      <path fill="var(--paper)" d="M0,477 Q429,303 858,477 Q429,359 0,477 Z"/>
      <polygon fill="var(--glacier)" points="0,240 208,477 165,477 0,288"/>
      <polygon fill="var(--glacier)" points="858,240 650,477 693,477 858,288"/>
    </svg>

    <div class="wordmark wordmark--back">
      <span class="wordmark__primary">GRAINITE RIDGE</span>
      <span class="wordmark__secondary">HOLDINGS LLC</span>
    </div>

    <p class="tagline">Real Estate Investments</p>
  </section>

</main>
</body>
</html>
```